Need wine label for brand that is named: Casmerel Vineyards & Winery

Casmerel is a yoga way of breathing. In Sanskrit Casmerel means "flying up." I would like a creative wine label that articulates Casmerel. The label should include a graphic and the name Casmerel on one line and Vineyards & Winery in smaller print underneath Casmerel.

```html
<!DOCTYPE html>
<html lang="en">
<head>
<meta charset="utf-8">
<title>Casmerel Vineyards &amp; Winery – Wine Label</title>
<link href="https://fonts.googleapis.com/css2?family=Didact+Gothic&display=swap" rel="stylesheet">
<style>
  :root {
    --backdrop: #111111;
    --ink-rust: #b4410c;
    --glow-yellow: #fbe96a;
    --glow-teal: #4fd8c0;
    --glow-peach: #fde3c8;
    --glow-cream: #fff6e2;
    --glow-blush: #f4dcd8;
    --petal-orange: #e8742a;
    --petal-deep: #c9500f;
  }
  html, body {
    margin: 0;
    padding: 0;
    width: 1200px;
    height: 1200px;
    overflow: hidden;
    background: var(--backdrop);
  }
  .canvas {
    position: relative;
    width: 1200px;
    height: 1200px;
    background: var(--backdrop);
  }
  .label {
    position: absolute;
    left: 325px;
    top: 50px;
    width: 550px;
    height: 1100px;
    overflow: hidden;
    font-family: "Didact Gothic", "Century Gothic", sans-serif;
    color: var(--ink-rust);
    text-align: center;
    background:
      radial-gradient(circle at 8% 22%, var(--glow-teal) 0, rgba(79,216,192,0) 30%),
      radial-gradient(circle at 35% 40%, var(--glow-yellow) 0, rgba(251,233,106,0) 38%),
      radial-gradient(circle at 85% 15%, var(--glow-peach) 0, rgba(253,227,200,0) 35%),
      radial-gradient(circle at 10% 70%, #bfeee0 0, rgba(191,238,224,0) 28%),
      radial-gradient(circle at 95% 75%, #9ee9d8 0, rgba(158,233,216,0) 22%),
      radial-gradient(circle at 15% 95%, var(--glow-yellow) 0, rgba(251,233,106,0) 30%),
      radial-gradient(circle at 85% 98%, var(--glow-blush) 0, rgba(244,220,216,0) 30%),
      var(--glow-cream);
  }
  .label__vintage {
    position: absolute;
    top: 42px;
    left: 0;
    right: 0;
    margin: 0;
    font-size: 29px;
    letter-spacing: 1px;
    font-weight: 400;
  }
  .label__emblem {
    position: absolute;
    left: 0;
    top: 150px;
    width: 550px;
    height: 600px;
    background:
      radial-gradient(ellipse 48% 30% at 50% 72%, rgba(201,80,15,0.85) 0, rgba(232,116,42,0.55) 45%, rgba(232,116,42,0) 75%),
      radial-gradient(ellipse 45% 60% at 50% 45%, rgba(232,116,42,0.18) 0, rgba(232,116,42,0) 70%);
  }
  .label__name {
    position: absolute;
    top: 800px;
    left: 0;
    right: 0;
    margin: 0;
    font-size: 86px;
    line-height: 1;
    font-weight: 400;
    letter-spacing: -1px;
  }
  .label__subtitle {
    position: absolute;
    top: 892px;
    left: 0;
    right: 0;
    margin: 0;
    font-size: 46px;
    line-height: 1;
    font-weight: 400;
  }
  .label__details {
    position: absolute;
    top: 1005px;
    left: 0;
    right: 0;
    margin: 0;
    font-size: 27px;
    letter-spacing: 1px;
  }
</style>
</head>
<body>
  <main class="canvas">
    <section class="label">
      <p class="label__vintage">AGED 2010</p>
      <div class="label__emblem" role="img" aria-label="Illustration of a figure seated in a meditation pose before an open orange lotus flower with fine rising petal lines"></div>
      <h1 class="label__name">CASMEREL</h1>
      <p class="label__subtitle">vineyards &amp; winery</p>
      <p class="label__details">12% vol &nbsp;|&nbsp; 50cl</p>
    </section>
  </main>
</body>
</html>
```